Vellum Systemics Buisness Cards

I need a technology focused clean business card for my employees. I have attached out logo to include in the mocks. We're a modern tech consulting firm that drives to interface humanity with technology in a truly cohesive fashion.

```html
<!DOCTYPE html>
<html lang="en">
<head>
<meta charset="utf-8">
<title>Vellum Systemics Business Card</title>
<link href="https://fonts.googleapis.com/css2?family=Fira+Sans:wght@500&family=Roboto:wght@400;500&display=swap" rel="stylesheet">
<style>
  :root {
    --page-bg: #e9e6e1;
    --card-clear: #eef0f1;
    --card-clear-edge: #dfe3e6;
    --card-blue: #2b6aa5;
    --card-blue-deep: #1f5a93;
    --curve-line: #2a2d33;
    --logo-grey: #6c6f75;
    --logo-blue: #2f6fb0;
    --name-tan: #ead8b8;
    --title-tan: #e1d3bb;
    --contact-white: #f1f3f5;
    --address-tan: #c9b896;
  }
  * { margin: 0; padding: 0; box-sizing: border-box; }
  html, body { width: 1200px; height: 1054px; overflow: hidden; }
  body {
    background: var(--page-bg);
    position: relative;
    font-family: "Roboto", Arial, sans-serif;
  }
  .business-card {
    position: absolute;
    left: 100px;
    top: 225px;
    width: 1000px;
    height: 603px;
    overflow: hidden;
    box-shadow: 0 18px 40px rgba(0,0,0,0.18);
  }
  .card-shapes { position: absolute; inset: 0; }
  .brand {
    position: absolute;
    left: 70px;
    top: 282px;
    display: flex;
    align-items: center;
    gap: 14px;
  }
  .brand-dot {
    width: 26px;
    height: 26px;
    border-radius: 50%;
    border: 5px solid var(--logo-blue);
  }
  .brand-name {
    font-family: "Roboto", Arial, sans-serif;
    font-weight: 500;
    font-size: 34px;
    color: var(--logo-grey);
    letter-spacing: 0.5px;
  }
  .contact-block {
    position: absolute;
    left: 600px;
    top: 160px;
  }
  .person-name {
    font-family: "Fira Sans", Arial, sans-serif;
    font-weight: 500;
    font-size: 33px;
    color: var(--name-tan);
    line-height: 1.1;
  }
  .person-title {
    font-size: 24px;
    color: var(--title-tan);
    margin-top: 8px;
  }
  .contact-list { list-style: none; margin-top: 32px; }
  .contact-item {
    display: flex;
    align-items: center;
    gap: 14px;
    font-size: 25px;
    color: var(--contact-white);
    height: 34px;
  }
  .contact-icon { width: 20px; height: 20px; flex: none; }
  .address {
    margin-top: 12px;
    font-size: 23px;
    line-height: 34px;
    color: var(--address-tan);
  }
</style>
</head>
<body>
  <div class="business-card">
    <svg class="card-shapes" width="1000" height="603" viewBox="0 0 1000 603">
      <defs>
        <linearGradient id="clearFace" x1="0" y1="0" x2="1" y2="1">
          <stop offset="0" stop-color="var(--card-clear)"/>
          <stop offset="1" stop-color="var(--card-clear-edge)"/>
        </linearGradient>
        <linearGradient id="blueFace" x1="0" y1="0" x2="0" y2="1">
          <stop offset="0" stop-color="var(--card-blue)"/>
          <stop offset="1" stop-color="var(--card-blue-deep)"/>
        </linearGradient>
      </defs>
      <rect width="1000" height="603" fill="url(#clearFace)"/>
      <path d="M428 0 Q592 301 428 603 L1000 603 L1000 0 Z" fill="url(#blueFace)"/>
      <path class="panel-edge-accent" d="M504 250 Q516 300 510 301.5 Q510 452 428 603 L412 603 Q500 452 504 250 Z" fill="var(--curve-line)"/>
    </svg>

    <div class="brand">
      <span class="brand-dot"></span>
      <span class="brand-name">Vellum Systemics</span>
    </div>

    <div class="contact-block">
      <div class="person-name">John Doe Smith</div>
      <div class="person-title">Managing Director</div>
      <ul class="contact-list">
        <li class="contact-item">
          <svg class="contact-icon" viewBox="0 0 20 20"><path d="M2 7 Q10 1 18 7 L16 9 L13 7 L13 5 L7 5 L7 7 L4 9 Z M5 10 L15 10 L17 17 L3 17 Z" fill="var(--contact-white)"/></svg>
          555.555.5555
        </li>
        <li class="contact-item">
          <svg class="contact-icon" viewBox="0 0 20 20"><rect x="1" y="4" width="18" height="12" fill="var(--contact-white)"/><path d="M1 4 L10 11 L19 4" fill="none" stroke="var(--card-blue)" stroke-width="1.6"/></svg>
          johndoe@example.com
        </li>
        <li class="contact-item">
          <svg class="contact-icon" viewBox="0 0 20 20"><circle cx="10" cy="10" r="8" fill="none" stroke="var(--contact-white)" stroke-width="2"/><ellipse cx="10" cy="10" rx="3.5" ry="8" fill="none" stroke="var(--contact-white)" stroke-width="1.5"/><line x1="2" y1="10" x2="18" y2="10" stroke="var(--contact-white)" stroke-width="1.5"/></svg>
          www.yourwebsite.com
        </li>
      </ul>
      <div class="address">234 Anywhere St., Any City<br>Any Town, US 123456</div>
    </div>
  </div>
</body>
</html>
```